Copperleaf Motorized Shade Business Card

Hello, we've had our logo made. Now we are looking for a clean and cool looking business card. One side can just be the logo with any design elements that might look good with it. The other side will be Name, Phone Number and Email. There will not be an address on the card.

```html
<!DOCTYPE html>
<html lang="en">
<head>
<meta charset="utf-8">
<title>Copperleaf Motorized Shade – Business Card</title>
<link href="https://fonts.googleapis.com/css2?family=Montserrat:wght@500;600;700;800&display=swap" rel="stylesheet">
<style>
  :root {
    --navy: #0d3a78;
    --sky: #0aa6e8;
    --sun: #f7c21a;
    --slate: #6e8bbd;
    --paper: #ffffff;
    --paper-shade: #eef1f5;
    --strip: #dfe7f3;
    --backdrop: #e6e8eb;
  }
  html, body {
    margin: 0;
    padding: 0;
    width: 738px;
    height: 1200px;
    overflow: hidden;
    background: var(--backdrop);
    font-family: "Montserrat", Arial, sans-serif;
  }
  .sheet {
    width: 738px;
    height: 1200px;
    display: flex;
    flex-direction: column;
    align-items: center;
    justify-content: center;
    gap: 64px;
  }
  .card {
    width: 620px;
    height: 334px;
    border-radius: 14px;
    overflow: hidden;
    box-shadow: 0 10px 26px rgba(13, 58, 120, 0.18);
    background: var(--paper);
  }
  .card svg { display: block; width: 100%; height: 100%; }
  .brand-name { font-weight: 800; fill: var(--navy); }
  .brand-tagline { font-weight: 700; fill: var(--sky); }
  .web-line { font-weight: 600; fill: var(--paper); font-size: 8.6px; }
  .contact-line { font-weight: 600; fill: var(--paper); font-size: 5.6px; }
  .person-name { font-weight: 800; fill: var(--paper); font-size: 5.6px; }
  .contact-icon { fill: none; stroke: var(--paper); stroke-width: 0.7; }
</style>
</head>
<body>
<main class="sheet">

  <section class="card card-front" aria-label="Business card front">
    <svg viewBox="0 0 390 210" xmlns="http://www.w3.org/2000/svg">
      <defs>
        <linearGradient id="paperFront" x1="0" y1="0" x2="1" y2="1">
          <stop offset="0" stop-color="var(--paper)"/>
          <stop offset="1" stop-color="var(--paper-shade)"/>
        </linearGradient>
      </defs>
      <rect class="paper" width="390" height="210" fill="url(#paperFront)"/>
      <polygon class="navy-wedge" points="310,0 390,0 390,210 220,210" fill="var(--navy)"/>

      <polygon class="web-band" points="0,174 196,174 188,198 0,198" fill="var(--sky)"/>
      <polygon class="sun-bar" points="200,174 212,174 199,210 187,210" fill="var(--sun)"/>
      <polygon class="sky-bar" points="216,174 305,174 297,198 208,198" fill="var(--sky)"/>
      <polygon class="sun-bar" points="338,172 358,172 345,210 325,210" fill="var(--sun)"/>
      <polygon class="paper-bar" points="365,172 382,172 369,210 352,210" fill="var(--paper)"/>

      <g class="brand-lockup">
        <rect class="brand-mark" x="38" y="38" width="26" height="26" fill="var(--sky)"/>
        <text class="brand-name" x="72" y="62" font-size="25">COPPERLEAF</text>
        <text class="brand-tagline" x="73" y="77" font-size="8.2" letter-spacing="2.1">MOTORIZED SHADES</text>
      </g>

      <text class="web-line" x="22" y="189">www.copperleafshades.com</text>
    </svg>
  </section>

  <section class="card card-back" aria-label="Business card back">
    <svg viewBox="0 0 390 210" xmlns="http://www.w3.org/2000/svg">
      <rect class="paper" width="390" height="210" fill="var(--paper)"/>
      <polygon class="navy-wedge" points="300,0 390,0 390,83 268,83" fill="var(--navy)"/>
      <polygon class="navy-bar" points="268,10 280,10 260,58 248,58" fill="var(--navy)"/>

      <rect class="navy-base" x="0" y="138" width="390" height="72" fill="var(--navy)"/>
      <polygon class="contact-band" points="0,83 372,83 352,138 0,138" fill="var(--sky)"/>
      <polygon class="paper-bar" points="372,88 386,88 368,136 354,136" fill="var(--paper)"/>
      <polygon class="paper-strip" points="0,143 294,143 291,150 0,150" fill="var(--strip)"/>

      <polygon class="slate-panel" points="58,150 212,150 192,210 38,210" fill="var(--slate)"/>
      <polygon class="sun-bar" points="222,150 252,150 232,210 202,210" fill="var(--sun)"/>
      <polygon class="sun-bar" points="260,150 292,150 272,210 240,210" fill="var(--sun)"/>
      <polygon class="sun-bar" points="362,200 390,200 390,210 358,210" fill="var(--sun)"/>

      <g class="brand-lockup">
        <rect class="brand-mark" x="24" y="16" width="20" height="20" fill="var(--sky)"/>
        <text class="brand-name" x="50" y="35" font-size="17">COPPERLEAF</text>
        <text class="brand-tagline" x="51" y="45" font-size="5.6" letter-spacing="1.5">MOTORIZED SHADES</text>
      </g>

      <g class="contact-left">
        <circle class="contact-icon" cx="28" cy="97.8" r="1.6"/>
        <path class="contact-icon" d="M25,103.5 c0,-2.2 1.3,-3.3 3,-3.3 s3,1.1 3,3.3"/>
        <text class="person-name" x="37" y="100.5">DANIEL HARTLEY</text>
        <text class="contact-line" x="37" y="108">Shade Consultant</text>

        <rect class="contact-icon" x="25" y="118.5" width="6" height="4.2"/>
        <path class="contact-icon" d="M25,118.5 l3,2.4 l3,-2.4"/>
        <text class="contact-line" x="37" y="122.6">hello@copperleafshades.com</text>
      </g>

      <line x1="168" y1="92" x2="168" y2="130" stroke="var(--paper)" stroke-width="0.5" opacity="0.8"/>

      <g class="contact-right">
        <path class="contact-icon" d="M184,94 l1.6,-0.4 l1,2 l-1,0.9 a5,5 0 0 0 2.3,2.3 l0.9,-1 l2,1 l-0.4,1.6 a6.5,6.5 0 0 1 -6.4,-6.4 z"/>
        <text class="contact-line" x="196" y="99">541-555-0172</text>

        <path class="contact-icon" d="M184,104.5 l1.6,-0.4 l1,2 l-1,0.9 a5,5 0 0 0 2.3,2.3 l0.9,-1 l2,1 l-0.4,1.6 a6.5,6.5 0 0 1 -6.4,-6.4 z"/>
        <text class="contact-line" x="196" y="109.5">541-555-0348</text>

        <circle class="contact-icon" cx="187.5" cy="119" r="3.2"/>
        <ellipse class="contact-icon" cx="187.5" cy="119" rx="1.3" ry="3.2"/>
        <line class="contact-icon" x1="184.3" y1="119" x2="190.7" y2="119"/>
        <text class="contact-line" x="196" y="121">www.copperleafshades.com</text>
      </g>
    </svg>
  </section>

</main>
</body>
</html>
```